marketing material folder

I need a folder design that has to inside pockets for distribution of business information and marketing materials

Target Market(s)

Limbcraft Partners referral sources such as physicians, physical therapy clinics and hospitals

Industry/Entity Type

Business

Requirements
Must have
• Similar but not exact design as my brochure project. Must have two pockets on the inside. Must have business card Holder on one of the pockets .
• Addresses and phone numbers for all locations from brochure on the back of folder

```html
<!DOCTYPE html>
<html lang="en">
<head>
<meta charset="utf-8">
<title>Limbcraft Partners – Presentation Folder</title>
<link href="https://fonts.googleapis.com/css2?family=Poppins:wght@500;600&family=Roboto:wght@400;700&display=swap" rel="stylesheet">
<style>
  :root{
    --paper:#ffffff;
    --charcoal:#3a3a3c;
    --charcoal-deep:#2e2e30;
    --silver:#b9babd;
    --silver-light:#dcdcde;
    --cover-red:#c2343a;
    --cover-red-deep:#a9282e;
    --pocket-red:#be1e2d;
    --pocket-red-light:#d8242f;
    --salmon:#c98a80;
    --cut-line:#29abe2;
    --ink-light:#ffffff;
  }
  html,body{margin:0;padding:0;width:1200px;height:818px;overflow:hidden;background:var(--paper);}
  .folder-dieline{display:block;width:1200px;height:818px;}
  .office-heading{font-family:"Roboto",sans-serif;font-weight:700;font-size:8.5px;fill:var(--ink-light);}
  .office-line{font-family:"Roboto",sans-serif;font-weight:400;font-size:6.2px;fill:var(--ink-light);}
  .brand-name{font-family:"Poppins",sans-serif;font-weight:500;font-size:19px;fill:var(--ink-light);}
  .icon{fill:none;stroke:var(--ink-light);stroke-width:0.7;}
  .icon-solid{fill:var(--ink-light);}
</style>
</head>
<body>
<svg class="folder-dieline" viewBox="0 0 1200 818" xmlns="http://www.w3.org/2000/svg">
  <defs>
    <clipPath id="back-panel-clip"><rect x="178" y="38" width="420" height="560"/></clipPath>
    <clipPath id="left-pocket-clip"><rect x="178" y="598" width="410" height="187"/></clipPath>
    <linearGradient id="runner-photo-tone" x1="0" y1="0" x2="0" y2="1">
      <stop offset="0" stop-color="#4a4a4c"/>
      <stop offset="0.6" stop-color="#3e3e40"/>
      <stop offset="1" stop-color="#545456"/>
    </linearGradient>
    <linearGradient id="leap-photo-tone" x1="0" y1="0" x2="0" y2="1">
      <stop offset="0" stop-color="#c4383e"/>
      <stop offset="0.7" stop-color="#bd3238"/>
      <stop offset="1" stop-color="var(--cover-red-deep)"/>
    </linearGradient>
  </defs>

  <!-- side glue flaps -->
  <path class="glue-flap glue-flap--left" d="M178 414 L143 427 L143 586 L178 586 Z" fill="var(--charcoal)"/>
  <path class="glue-flap glue-flap--right" d="M1018 414 L1053 427 L1053 586 L1018 586 Z" fill="var(--cover-red)"/>

  <!-- back cover panel -->
  <g class="back-cover" clip-path="url(#back-panel-clip)">
    <rect x="178" y="38" width="420" height="560" fill="var(--charcoal)"/>
    <rect class="runner-photo" x="178" y="90" width="300" height="508" fill="url(#runner-photo-tone)" role="img" aria-label="Black and white photo of an athlete running with a prosthetic blade leg"/>
    <path class="wave-silver" d="M508 38 C530 120 520 200 520 260 C520 340 540 420 500 500 C480 540 460 570 440 598 L598 598 L598 38 Z" fill="var(--silver)"/>
    <path class="wave-silver-light" d="M522 38 C540 120 532 200 532 260 C532 340 552 420 512 500 C492 540 472 570 452 598 L598 598 L598 38 Z" fill="var(--silver-light)"/>
    <path class="wave-red" d="M592 38 C552 130 540 210 543 270 C546 350 560 430 522 505 C504 545 488 575 470 598 L598 598 L598 38 Z" fill="var(--cover-red)"/>
  </g>

  <!-- office locations -->
  <g class="office-locations">
    <text class="office-heading" x="426" y="314">Office Locations:</text>
    <g class="office office--memphis">
      <path class="icon" d="M429 326 a2.3 2.3 0 1 1 0.01 0 Z M429 330.5 l-2.1 -3.4 M429 330.5 l2.1 -3.4"/>
      <text class="office-line" x="436" y="331">4820 Linden Avenue,</text>
      <text class="office-line" x="436" y="338.5">Ste 210</text>
      <text class="office-line" x="436" y="346">Memphis, TN 38117</text>
      <path class="icon" d="M427 349.5 q0 4 4 4 l0.6 -1.2 -1.3 -0.9 -0.8 0.8 q-1.6 -0.8 -2.2 -2.2 l0.8 -0.8 -0.9 -1.3 Z"/>
      <text class="office-line" x="436" y="354">(901) 555 - 0142</text>
      <rect class="icon-solid" x="427" y="357.5" width="4.4" height="4.4" rx="0.6"/>
      <text class="office-line" x="436" y="361.5">(901) 555 - 0143</text>
    </g>
    <g class="office office--houston">
      <path class="icon" d="M429 372 a2.3 2.3 0 1 1 0.01 0 Z M429 376.5 l-2.1 -3.4 M429 376.5 l2.1 -3.4"/>
      <text class="office-line" x="436" y="377">9270 Briarstone Lane,</text>
      <text class="office-line" x="436" y="384.5">Ste B</text>
      <text class="office-line" x="436" y="392">Houston, TX 77063</text>
      <path class="icon" d="M427 395.5 q0 4 4 4 l0.6 -1.2 -1.3 -0.9 -0.8 0.8 q-1.6 -0.8 -2.2 -2.2 l0.8 -0.8 -0.9 -1.3 Z"/>
      <text class="office-line" x="436" y="400">(281) 555 - 0176</text>
      <rect class="icon-solid" x="427" y="403.5" width="4.4" height="4.4" rx="0.6"/>
      <text class="office-line" x="436" y="407.5">(281) 555 - 0177</text>
    </g>
    <g class="office office--arlington">
      <path class="icon" d="M429 418 a2.3 2.3 0 1 1 0.01 0 Z M429 422.5 l-2.1 -3.4 M429 422.5 l2.1 -3.4"/>
      <text class="office-line" x="436" y="423">2408 Harwood Road,</text>
      <text class="office-line" x="436" y="430.5">Ste 300</text>
      <text class="office-line" x="436" y="438">Arlington, TX 76018</text>
      <path class="icon" d="M427 441.5 q0 4 4 4 l0.6 -1.2 -1.3 -0.9 -0.8 0.8 q-1.6 -0.8 -2.2 -2.2 l0.8 -0.8 -0.9 -1.3 Z"/>
      <text class="office-line" x="436" y="446">(682) 555 - 0191</text>
      <rect class="icon-solid" x="427" y="449.5" width="4.4" height="4.4" rx="0.6"/>
      <text class="office-line" x="436" y="453.5">(682) 555 - 0192</text>
    </g>
  </g>

  <!-- front cover panel -->
  <g class="front-cover">
    <rect x="598" y="38" width="420" height="560" fill="var(--cover-red)"/>
    <rect class="leap-photo" x="598" y="38" width="420" height="560" fill="url(#leap-photo-tone)" role="img" aria-label="Red-toned photo of an athlete with a prosthetic leg leaping over rocks by a lake"/>
    <g class="front-brand">
      <circle cx="842" cy="520" r="20" fill="none" stroke="var(--ink-light)" stroke-width="3"/>
      <text class="brand-name" x="868" y="527">Limbcraft Partners</text>
    </g>
  </g>

  <!-- left inside pocket -->
  <g class="pocket pocket--left" clip-path="url(#left-pocket-clip)">
    <rect x="178" y="598" width="410" height="187" fill="var(--charcoal)"/>
    <path d="M440 598 C410 650 340 720 322 785 L588 785 L588 598 Z" fill="var(--silver)"/>
    <path d="M470 598 C440 660 390 720 380 785 L588 785 L588 598 Z" fill="var(--salmon)"/>
    <path d="M490 598 C460 660 420 720 412 785 L588 785 L588 598 Z" fill="var(--pocket-red)"/>
    <path d="M545 598 C560 660 575 720 568 785 L588 785 L588 598 Z" fill="var(--pocket-red-light)" opacity="0.7"/>
    <g class="pocket-brand" transform="rotate(180 281 659)">
      <circle cx="330" cy="658" r="20" fill="none" stroke="var(--ink-light)" stroke-width="3"/>
      <text class="brand-name" x="304" y="655" text-anchor="end">Limbcraft</text>
      <text class="brand-name" x="304" y="676" text-anchor="end">Partners</text>
    </g>
  </g>

  <!-- right inside pocket with card holder -->
  <g class="pocket pocket--right">
    <rect x="608" y="598" width="410" height="187" fill="var(--pocket-red)"/>
    <path d="M612 598 C640 660 650 730 640 785 L660 785 C670 720 660 650 636 598 Z" fill="var(--pocket-red-light)" opacity="0.8"/>
    <path d="M700 598 C740 660 720 730 715 785 L735 785 C745 720 760 650 722 598 Z" fill="var(--pocket-red-light)" opacity="0.7"/>
    <path d="M940 598 C910 660 905 720 920 785 L1018 785 L1018 598 Z" fill="var(--pocket-red-light)"/>
    <g class="card-holder-slits" stroke="#a81a27" stroke-width="0.8" fill="none">
      <path d="M728 662 L748 642"/>
      <path d="M872 642 L892 662"/>
    </g>
  </g>
  <path class="pocket-gap" d="M596 598 L600 598 L608 785 L588 785 Z" fill="var(--paper)"/>

  <!-- die lines -->
  <g class="die-lines" fill="none" stroke="var(--cut-line)" stroke-width="0.8">
    <path d="M178 38 L1018 38"/>
    <path d="M598 38 L598 598" stroke-dasharray="4 3"/>
    <path d="M178 414 L178 586" stroke="#6a6a6c" stroke-dasharray="3 3"/>
    <path d="M1018 414 L1018 586" stroke="#e06a6e" stroke-dasharray="3 3"/>
  </g>
</svg>
</body>
</html>
```